Visitenkarten für Wahlärztin
Zielgruppe
Ich bin Ärztin für Allgemeinmedizin. Mein Schwerpunkt liegt auf Akupunktur und Manuelle Medizin. Als Wahlärztin sind meine Zielgruppe Privatpatienten - Primär Erwachsene, aber auch Kinder.
Aufgabenstellung
Logo (ev. nur Zeichen) und Informationen auf der Visitenkarte:
Dr. Gerlinde Wassmuthner
Ärztin für Allgemeinmedizin
Akupunktur
Manuelle Medizin
Lindauerstraße 7
3512 Auental an der Donau
praxis@dr-wassmuthner-beispiel.at
www.dr-wassmuthner-beispiel.at
Wahlärztin
Termin nach telefonischer Vereinbarung
Das Design soll das edle Logo mit Natürlichkeit/Leichtigkeit verbinden bzw. erden und ganzheitliche Medizin im verkörpern.

```html
<!DOCTYPE html>
<html lang="de">
<head>
<meta charset="utf-8">
<title>Visitenkarte Dr. Gerlinde Wassmuthner</title>
<link rel="stylesheet" href="https://fonts.googleapis.com/css2?family=Tenor+Sans&family=Questrial&family=Arimo&display=swap">
<style>
  :root {
    --backdrop: #3e3d3b;
    --card: #ffffff;
    --gold: #b8862a;
    --gold-dark: #9c6f1c;
    --gold-light: #ecc766;
    --ink: #4a4a4a;
    --ink-soft: #5a5a5a;
  }
  * { margin: 0; padding: 0; box-sizing: border-box; }
  html, body {
    width: 1200px; height: 900px; overflow: hidden;
    background: var(--backdrop);
  }
  .card {
    position: absolute; left: 292px; width: 634px;
    background: var(--card);
  }
  .card::after {
    content: ""; position: absolute; left: 0; right: 0; bottom: 0; height: 6px;
    background: linear-gradient(90deg, var(--gold-dark), var(--gold) 40%, var(--gold-light) 68%, var(--gold) 85%, var(--gold-dark));
  }
  .card--front { top: 43px; height: 380px; }
  .card--back { top: 474px; height: 371px; }

  .mark { position: absolute; }
  .mark__label {
    font-family: "Tenor Sans", sans-serif; fill: var(--gold);
  }

  .front__name {
    position: absolute; top: 240px; left: 0; right: 0; text-align: center;
    font-family: "Tenor Sans", sans-serif; font-weight: 400; font-size: 38px; color: var(--gold);
    letter-spacing: 0.5px;
  }
  .front__title {
    position: absolute; top: 287px; left: 0; right: 0; text-align: center;
    font-family: "Tenor Sans", sans-serif; font-size: 15px; color: var(--ink);
  }

  .back__role {
    position: absolute; left: 54px; top: 96px;
    font-family: "Arimo", sans-serif; font-weight: 400; font-size: 28px; color: var(--gold);
    letter-spacing: 1.5px;
  }
  .back__note {
    position: absolute; left: 54px; top: 139px;
    font-family: "Arimo", sans-serif; font-size: 16.5px; color: var(--ink);
  }
  .back__rule {
    position: absolute; left: 58px; width: 513px; top: 204px; height: 2px;
    background: #d2ad63;
  }
  .contact-list { position: absolute; left: 54px; top: 228px; list-style: none; }
  .contact-list li {
    display: flex; align-items: center; height: 23px;
    font-family: "Questrial", sans-serif; font-size: 19px; color: var(--ink);
  }
  .contact-list svg { width: 18px; height: 16px; margin-right: 15px; flex: none; }
  .back__address {
    position: absolute; left: 54px; top: 321px;
    font-family: "Questrial", sans-serif; font-size: 20px; color: var(--ink-soft);
  }
  .back__address .sep { color: var(--gold); margin: 0 4px; }
</style>
</head>
<body>

<section class="card card--front">
  <svg class="mark" style="left:240px;top:86px" width="154" height="154" viewBox="0 0 154 154" aria-label="Praxiszeichen">
    <circle cx="77" cy="77" r="70" fill="none" stroke="var(--gold)" stroke-width="5"/>
    <text class="mark__label" x="77" y="83" text-anchor="middle" font-size="17">Wassmuthner</text>
  </svg>
  <h1 class="front__name">Dr. Gerlinde Wassmuthner</h1>
  <p class="front__title">Ärztin für Allgemeinmedizin und Akupunktur</p>
</section>

<section class="card card--back">
  <svg class="mark" style="left:459px;top:53px" width="118" height="118" viewBox="0 0 118 118" aria-label="Praxiszeichen">
    <circle cx="59" cy="59" r="55" fill="none" stroke="var(--gold)" stroke-width="4"/>
    <text class="mark__label" x="59" y="64" text-anchor="middle" font-size="13">Wassmuthner</text>
  </svg>

  <h2 class="back__role">Wahlärztin</h2>
  <p class="back__note">Termine nach telefonischer Vereinbarung</p>
  <div class="back__rule"></div>

  <ul class="contact-list">
    <li>
      <svg viewBox="0 0 18 16"><path d="M3 1.5 L6 1 L7.5 4.5 L5.6 6 Q7.5 10 11 11.4 L12.6 9.6 L16 11 L15.6 14 Q9 15 4.5 9.5 Q1.5 5.5 3 1.5 Z" fill="var(--gold)"/></svg>
      +43 660 482 17 930
    </li>
    <li>
      <svg viewBox="0 0 18 16"><rect x="1" y="3" width="16" height="10" fill="var(--gold)"/><path d="M1 3 L9 9 L17 3 M1 13 L7 8 M17 13 L11 8" stroke="#fff" stroke-width="1.2" fill="none"/></svg>
      praxis@dr-wassmuthner-beispiel.at
    </li>
    <li>
      <svg viewBox="0 0 18 16"><g fill="none" stroke="var(--gold)" stroke-width="1.1"><circle cx="9" cy="8" r="7"/><ellipse cx="9" cy="8" rx="3" ry="7"/><path d="M2 8 H16 M3 4.5 H15 M3 11.5 H15"/></g></svg>
      www.dr-wassmuthner-beispiel.at
    </li>
  </ul>

  <p class="back__address">Lindauerstraße 7<span class="sep">|</span>3512 Auental an der Donau</p>
</section>

</body>
</html>
```